BrambleWorks business card

Looking for business card design that supports our company/software values. We have 2 logo designs at the moment but open to change if you think you can enhance the brand. Check out website www.brambleworks.com.au.

Target Market(s)

Education

Contact Information for Business Card

Name, title, mobile, email and website

Font styles to use
Sans Serif

Colors

Designer to choose colors to be used in the design.

Requirements
Must have
• BrambleWorks logo with tree and tagline on rear side with dark grey background colour

```html
<!DOCTYPE html>
<html lang="en">
<head>
<meta charset="utf-8">
<title>BrambleWorks business card</title>
<link href="https://fonts.googleapis.com/css2?family=Mulish:wght@400;500&family=Ubuntu:wght@400;500&display=swap" rel="stylesheet">
<style>
  :root {
    --page: #ffffff;
    --paper: #efefeb;
    --ink: #3f403f;
    --ink-soft: #555755;
    --slate: #575a58;
    --back: #4a4c4b;
    --back-ink: #f1f1ed;
    --back-ink-soft: #d6d8d4;
    --leaf: #4f7f3a;
    --leaf-light: #6fa052;
  }
  * { margin: 0; padding: 0; box-sizing: border-box; }
  html, body { width: 900px; height: 1200px; overflow: hidden; background: var(--page); }
  .canvas { position: relative; width: 900px; height: 1200px; }

  .card {
    position: absolute; left: 78px; width: 758px; height: 432px;
    background: var(--paper);
  }
  .card--front { top: 133px; }
  .card--back { top: 638px; background: var(--back); }

  /* front */
  .brand-lockup {
    position: absolute; left: 0; width: 376px; top: 150px;
    display: flex; flex-direction: column; align-items: center; gap: 38px;
  }
  .brand-mark { display: block; width: 40px; height: 40px; border-radius: 50%; background: var(--leaf); }
  .brand-name {
    font-family: "Ubuntu", sans-serif; font-weight: 400;
    font-size: 34px; line-height: 1; color: #2f302f;
  }
  .divider {
    position: absolute; left: 372px; top: 108px; width: 1px; height: 218px;
    background: var(--ink);
  }
  .contact {
    position: absolute; left: 425px; top: 110px;
    font-family: "Mulish", sans-serif; color: var(--ink-soft);
  }
  .contact__name { font-size: 28px; font-weight: 400; letter-spacing: 0.5px; color: var(--ink); line-height: 1; }
  .contact__title { font-size: 16px; margin-top: 8px; font-weight: 500; }
  .contact__address { font-size: 16px; line-height: 21px; margin-top: 18px; }
  .contact__list { list-style: none; margin-top: 14px; font-size: 16px; line-height: 21.5px; }
  .contact__list li { display: flex; align-items: center; gap: 8px; }
  .contact__list svg { width: 12px; height: 12px; fill: var(--ink); flex: none; }

  .band { position: absolute; bottom: 0; height: 21px; }
  .band--slate { left: 0; width: 377px; background: var(--slate); }
  .band--leaf { left: 380px; right: 0; background: var(--leaf); }

  /* back */
  .back-lockup {
    position: absolute; left: 0; right: 0; top: 160px;
    display: flex; align-items: center; justify-content: center; gap: 26px;
  }
  .back-lockup .brand-mark { width: 44px; height: 44px; background: var(--leaf-light); }
  .back-lockup__text { display: flex; flex-direction: column; align-items: center; }
  .back-lockup__name {
    font-family: "Ubuntu", sans-serif; font-weight: 400; font-size: 52px;
    color: var(--back-ink); line-height: 1;
  }
  .back-lockup__rule { width: 100%; height: 2px; background: var(--back-ink-soft); margin: 12px 0 8px; }
  .tagline { font-family: "Ubuntu", sans-serif; font-size: 23px; color: var(--back-ink-soft); }
  .web {
    position: absolute; left: 0; right: 0; bottom: 28px; text-align: center;
    font-family: "Mulish", sans-serif; font-size: 16px; letter-spacing: 3px; color: var(--back-ink);
  }
</style>
</head>
<body>
<main class="canvas">

  <section class="card card--front" aria-label="Card front">
    <div class="brand-lockup">
      <span class="brand-mark"></span>
      <span class="brand-name">BrambleWorks</span>
    </div>
    <div class="divider"></div>
    <div class="contact">
      <p class="contact__name">CLARA DENHOLM</p>
      <p class="contact__title">CEO/ Founder</p>
      <p class="contact__address">14th floor, Corvel<br>Tower CDMX</p>
      <ul class="contact__list">
        <li><svg viewBox="0 0 24 24"><path d="M6.6 10.8a15.1 15.1 0 0 0 6.6 6.6l2.2-2.2c.3-.3.7-.4 1-.2 1.1.4 2.3.6 3.6.6.6 0 1 .4 1 1V20c0 .6-.4 1-1 1A17 17 0 0 1 3 4c0-.6.4-1 1-1h3.5c.6 0 1 .4 1 1 0 1.3.2 2.5.6 3.6.1.3 0 .7-.2 1z"/></svg>(55) 4812 6640 ext. 1 27</li>
        <li><svg viewBox="0 0 24 24"><path d="M2 8c2-3 6-4 10-4s8 1 10 4l-3 3-4-1V8H9v2l-4 1zM5 13h14l2 7H3zm7 2a2 2 0 1 0 0 4 2 2 0 0 0 0-4z"/></svg>56 2294 0718</li>
        <li><svg viewBox="0 0 24 24"><path d="M2 5h20v14H2zm2 2v.4l8 5.6 8-5.6V7z"/></svg>clara.d@brambleworks.com</li>
        <li><svg viewBox="0 0 24 24"><path d="M12 2a7 7 0 0 0-7 7c0 5 7 13 7 13s7-8 7-13a7 7 0 0 0-7-7zm0 9.5a2.5 2.5 0 1 1 0-5 2.5 2.5 0 0 1 0 5z"/></svg>14th floor, Corvel Tower CDMX</li>
      </ul>
    </div>
    <div class="band band--slate"></div>
    <div class="band band--leaf"></div>
  </section>

  <section class="card card--back" aria-label="Card back">
    <div class="back-lockup">
      <span class="brand-mark"></span>
      <div class="back-lockup__text">
        <span class="back-lockup__name">BrambleWorks</span>
        <span class="back-lockup__rule"></span>
        <span class="tagline">Student Success Platform</span>
      </div>
    </div>
    <p class="web">www.brambleworks.com.au</p>
  </section>

</main>
</body>
</html>
```